The Hollow Pines - Short Film Poster Design

A short film that follows a forest ranger contemplating suicide as he stumbles upon three kids lost in the forest, each in their own, different way.

Genre: Contemporary Dark Drama

Seeking a poster that really stands out as a 'Festival Piece'. See the following lists for references:

Brindlecove Festival Poster Awards: https://www.snapvault.example/photos/officialbrcv/with/48203917265/

Here is the FULL RESOLUTION short film to take screen grabs and reference photos from:
https://www.boxdrift.example/s/qwet83jd02kfm7z/Reel027.mov?oref=e

We are open to much of anything, but this project needs to stand out as unique. On top of that, we are trying to push the angle of strangers LOST in the forest (hence the name) and have thought of the opening sequence of the young man walking through the woods on the epic wide shot of being used for the poster art.

Various items need to be included on the poster: (Please feel free to reword as appropriate)

1) A FILM BY OSWIN HARTLEY
2) A TOBIAS GRUNWELL PRODUCTION

All other taglines are optional and subject to addition or removal.

Please message with all other questions and comments.
Updates

Hey everyone, I apologize for not providing a high enough resolution copy of the short. I was told that this was the highest resolution until I got back straight from my editor who said it's a preliminary. Unfortunately, I do not have the ENTIRE film at top resolution. I will, however, attach high resolution .tiffs from various points of the film for use. https://www.boxdrift.example/sh/pzmk47tyeo81gd/BBXQwuLpoNZdFhVc27kjsTmqe?dl=0

Industry/Entity Type

Film Production

Font styles to use
Serif
Sans Serif

Requirements
Must have
• 1) A FILM BY OSWIN HARTLEY
• 2) A TOBIAS GRUNWELL PRODUCTION
• "THE HOLLOW PINES" - Name of Film
Nice to have
• Tagline, but not necessary.

```html
<!DOCTYPE html>
<html lang="en">
<head>
<meta charset="utf-8">
<title>The Hollow Pines — Poster</title>
<link href="https://fonts.googleapis.com/css2?family=Noto+Serif:ital,wght@0,400;0,700;1,400;1,700&display=swap" rel="stylesheet">
<style>
  :root {
    --night: #0c0f12;
    --forest: #1b2419;
    --leaf-light: #4a5240;
    --taupe: #998778;
    --paper: #f4f2f0;
    --outline: rgba(190, 180, 170, 0.45);
  }
  * { margin: 0; padding: 0; box-sizing: border-box; }
  html, body { width: 810px; height: 1200px; overflow: hidden; background: var(--night); }
  .poster {
    position: relative;
    width: 810px;
    height: 1200px;
    overflow: hidden;
    font-family: "Noto Serif", Georgia, serif;
    color: var(--paper);
  }
  .scene {
    position: absolute;
    inset: 0;
    background:
      radial-gradient(ellipse 70% 30% at 60% 78%, rgba(120, 118, 100, 0.35), transparent 70%),
      radial-gradient(ellipse 60% 40% at 80% 45%, rgba(60, 75, 55, 0.35), transparent 70%),
      linear-gradient(180deg, var(--night) 0%, var(--forest) 45%, #141811 70%, #22241d 100%);
  }
  .genre {
    position: absolute;
    left: 90px;
    top: 88px;
    font-size: 16px;
    font-variant: small-caps;
    letter-spacing: 0.5px;
    color: var(--paper);
  }
  .echo {
    position: absolute;
    font-style: italic;
    font-weight: 400;
    color: transparent;
    -webkit-text-stroke: 1px var(--outline);
    white-space: nowrap;
    line-height: 1;
  }
  .echo--large { left: 370px; top: -40px; font-size: 200px; }
  .echo--small { left: 598px; top: 205px; font-size: 104px; }
  .title { position: absolute; left: 62px; top: 150px; line-height: 1; }
  .title__lead {
    display: block;
    position: relative;
    z-index: 2;
    margin-left: 112px;
    font-size: 66px;
    font-style: italic;
    font-weight: 400;
    color: var(--paper);
    text-shadow: 0 2px 4px rgba(0,0,0,0.6);
  }
  .title__main {
    display: block;
    margin-top: -58px;
    font-size: 190px;
    font-style: italic;
    font-weight: 700;
    letter-spacing: -4px;
    background: linear-gradient(180deg, var(--taupe) 0%, var(--taupe) 60%, rgba(153,135,120,0.05) 100%);
    -webkit-background-clip: text;
    background-clip: text;
    color: transparent;
  }
  .credits {
    position: absolute;
    top: 476px;
    font-size: 24px;
    line-height: 1.45;
    font-style: italic;
  }
  .credits strong { font-weight: 700; }
  .credits--director { left: 70px; }
  .credits--producer { left: 366px; }
  .backdrop-word {
    position: absolute;
    left: -95px;
    top: 620px;
    font-size: 560px;
    font-style: italic;
    font-weight: 700;
    line-height: 1;
    letter-spacing: -10px;
    color: var(--taupe);
    white-space: nowrap;
  }
</style>
</head>
<body>
  <main class="poster">
    <div class="scene" role="img" aria-label="Night forest clearing lit by a flashlight, a fallen figure lying among leaves and brush"></div>

    <span class="echo echo--large" aria-hidden="true">pines</span>
    <span class="echo echo--small" aria-hidden="true">pines</span>

    <p class="genre">Contemporary Dark Drama</p>

    <h1 class="title">
      <span class="title__lead">the hollow</span>
      <span class="title__main">pines</span>
    </h1>

    <p class="credits credits--director">A Film by<br><strong>Oswin Hartley</strong></p>
    <p class="credits credits--producer">A <strong>Tobias Grunwell</strong><br><strong>Production</strong></p>

    <span class="backdrop-word" aria-hidden="true">pin</span>
  </main>
</body>
</html>
```